Verdal Group Business Card Design

The CEO is looking for a new trendy look for his business card.
You can stay with current branding or come up with something new/creative. It can be 3D, including Medical Office buildings. You can use our logo in a variety of colors. Please include name, title, company name, company website, email address, cell number

Target Market(s)

Real Estate Development and Construction

Industry/Entity Type

Health care real estate

Contact Information for Business Card

Rohesh Kamble, CEO M-702.418.6293 E-roheshkamble@verdal.example Address:4100 Lanyard St, Tampa, FL 33611 www.verdal.example

Other font styles liked:
• Be creative

Requirements
Must have
• Creative, trendy look
Nice to have
• Please go to our website to get a feel- www. verdal.example
Should not have
• small fonts

```html
<!DOCTYPE html>
<html lang="en">
<head>
<meta charset="utf-8">
<title>Verdal Group – Business Card</title>
<link href="https://fonts.googleapis.com/css2?family=Ubuntu:wght@400;700&display=swap" rel="stylesheet">
<style>
  :root {
    --stage: #2a2d31;
    --paper: #ffffff;
    --ink: #0d0d0d;
    --ink-soft: #1a1a1a;
    --rule: #222222;
    --back-base: #0a0a0a;
    --back-tone: #1c1c1c;
  }
  * { margin: 0; padding: 0; box-sizing: border-box; }
  html, body { width: 1200px; height: 900px; overflow: hidden; }
  body {
    background: var(--stage);
    font-family: "Ubuntu", Arial, sans-serif;
    display: flex;
    flex-direction: column;
    align-items: center;
    justify-content: center;
    gap: 56px;
  }
  .card {
    position: relative;
    width: 630px;
    height: 360px;
    overflow: hidden;
    box-shadow: 0 14px 36px rgba(0,0,0,0.45);
  }

  /* Front */
  .card-front { background: var(--paper); color: var(--ink); }
  .corner-bar { position: absolute; background: var(--ink); }
  .corner-bar--top { left: 0; top: 0; width: 92px; height: 22px; }
  .corner-bar--bottom { right: 0; bottom: 0; width: 148px; height: 34px; }

  .brand-name {
    position: absolute;
    left: 58px;
    top: 112px;
    width: 220px;
    font-weight: 700;
    font-size: 50px;
    line-height: 0.95;
    letter-spacing: -1.5px;
    color: var(--ink);
    text-align: right;
  }
  .divider {
    position: absolute;
    left: 300px;
    top: 100px;
    width: 1.5px;
    height: 190px;
    background: var(--rule);
  }
  .contact {
    position: absolute;
    left: 322px;
    top: 100px;
    color: var(--ink-soft);
  }
  .contact-name { font-weight: 700; font-size: 24px; line-height: 1.1; }
  .contact-title { font-size: 14px; margin-top: 4px; }
  .contact-address { font-size: 14px; line-height: 1.3; margin-top: 8px; }
  .contact-list { list-style: none; margin-top: 8px; }
  .contact-list li {
    display: flex;
    align-items: center;
    gap: 8px;
    font-size: 14px;
    line-height: 1.55;
  }
  .contact-list svg { width: 12px; height: 12px; flex: none; }

  /* Back */
  .card-back { background: var(--back-base); }
  .back-pattern {
    position: absolute;
    inset: 0;
    background: linear-gradient(150deg, var(--back-tone) 0%, var(--back-base) 55%, #050505 100%);
  }
  .back-brand {
    position: absolute;
    left: 0; right: 0;
    top: 150px;
    text-align: center;
    font-weight: 700;
    font-size: 40px;
    letter-spacing: -1px;
    color: var(--paper);
  }
</style>
</head>
<body>

  <section class="card card-front" aria-label="Business card front">
    <div class="corner-bar corner-bar--top"></div>
    <div class="corner-bar corner-bar--bottom"></div>

    <div class="brand-name">Verdal Group</div>
    <div class="divider"></div>

    <div class="contact">
      <p class="contact-name">Rohesh Kamble</p>
      <p class="contact-title">CEO</p>
      <p class="contact-address">4100 Lanyard St,<br>Tampa, FL 33611</p>
      <ul class="contact-list">
        <li>
          <svg viewBox="0 0 12 12" aria-hidden="true"><circle cx="6" cy="6" r="6" fill="#111"/><path d="M4 3.2c.4-.3.7-.2.9.2l.4.8c.1.3 0 .5-.2.7l-.3.3c.3.7.8 1.2 1.5 1.5l.3-.3c.2-.2.4-.3.7-.2l.8.4c.4.2.5.5.2.9-.6.8-1.5.8-2.6.1C4.6 6.9 3.9 6.2 3.4 5.1 3 4.3 3.2 3.7 4 3.2z" fill="#fff"/></svg>
          702.418.6293
        </li>
        <li>
          <svg viewBox="0 0 12 12" aria-hidden="true"><circle cx="6" cy="6" r="6" fill="#111"/><rect x="2.8" y="3.8" width="6.4" height="4.4" fill="none" stroke="#fff" stroke-width="0.9"/><path d="M2.8 3.8 6 6.4l3.2-2.6" fill="none" stroke="#fff" stroke-width="0.9"/></svg>
          roheshkamble@verdal.example
        </li>
        <li>
          <svg viewBox="0 0 12 12" aria-hidden="true"><circle cx="6" cy="6" r="6" fill="#111"/><circle cx="6" cy="6" r="3.4" fill="none" stroke="#fff" stroke-width="0.8"/><ellipse cx="6" cy="6" rx="1.4" ry="3.4" fill="none" stroke="#fff" stroke-width="0.8"/><path d="M2.6 6h6.8" stroke="#fff" stroke-width="0.8"/></svg>
          www.verdal.example
        </li>
      </ul>
    </div>
  </section>

  <section class="card card-back" aria-label="Business card back">
    <div class="back-pattern" role="img" aria-label="Repeating tone-on-tone brand name pattern in glossy black"></div>
    <div class="back-brand">Verdal Group</div>
  </section>

</body>
</html>
```